The Plate Compass

Cutting Through the Noise to What Actually Works.

Nutrition book

Target Market(s)

People looking to be or get healthy and eat right.

```html
<!DOCTYPE html>
<html lang="en">
<head>
<meta charset="utf-8">
<title>The Plate Compass</title>
<link href="https://fonts.googleapis.com/css2?family=Archivo+Black&family=Montserrat:wght@400;700&family=Oswald:wght@400&display=swap" rel="stylesheet">
<style>
  :root {
    --bg: #000000;
    --accent: #80ff00;
    --ink: #ffffff;
  }
  * { margin: 0; padding: 0; box-sizing: border-box; }
  html, body {
    width: 800px;
    height: 1200px;
    overflow: hidden;
    background: var(--bg);
  }
  .cover {
    position: relative;
    width: 800px;
    height: 1200px;
    background: var(--bg);
    overflow: hidden;
  }
  .title-line {
    position: absolute;
    left: 0;
    width: 800px;
    text-align: center;
    font-family: "Archivo Black", sans-serif;
    font-size: 112px;
    line-height: 1;
    letter-spacing: 6px;
    color: var(--accent);
    text-transform: uppercase;
  }
  .title-the { top: 51px; }
  .title-plate { top: 178px; }
  .title-compass { top: 304px; }
  .subtitle {
    position: absolute;
    left: 30px;
    width: 740px;
    top: 453px;
    text-align: center;
    font-family: "Montserrat", sans-serif;
    font-weight: 400;
    font-size: 27px;
    line-height: 40px;
    letter-spacing: 3px;
    color: var(--ink);
    text-transform: uppercase;
  }
  .pyramid {
    position: absolute;
    left: 0;
    top: 0;
    width: 800px;
    height: 1200px;
  }
  .tier { fill: var(--ink); }
  .marker { fill: var(--accent); }
  .marker-line { stroke: var(--accent); stroke-width: 3; }
  .tier-label {
    position: absolute;
    font-family: "Oswald", sans-serif;
    font-weight: 400;
    font-size: 22px;
    line-height: 26px;
    letter-spacing: 2px;
    color: var(--ink);
    text-transform: uppercase;
    white-space: nowrap;
  }
  .label-left { text-align: right; }
  .author {
    position: absolute;
    left: 0;
    width: 800px;
    top: 1117px;
    text-align: center;
    font-family: "Montserrat", sans-serif;
    font-weight: 700;
    font-size: 34px;
    line-height: 42px;
    letter-spacing: 2px;
    color: var(--ink);
    text-transform: uppercase;
  }
</style>
</head>
<body>
<main class="cover">
  <h1>
    <span class="title-line title-the">The</span>
    <span class="title-line title-plate">Plate</span>
    <span class="title-line title-compass">Compass</span>
  </h1>
  <p class="subtitle">Cutting through the noise to what<br>actually works</p>

  <svg class="pyramid" viewBox="0 0 800 1200" aria-label="Nutrition priority pyramid">
    <polygon class="tier" points="402,585 443.5,683 360.5,683"/>
    <polygon class="tier" points="355.4,695 448.6,695 468.4,742 335.6,742"/>
    <polygon class="tier" points="330.5,754 473.5,754 494.3,803 309.7,803"/>
    <polygon class="tier" points="305.1,814 498.9,814 518.4,860 285.6,860"/>
    <polygon class="tier" points="279.7,874 524.3,874 544.2,921 259.8,921"/>
    <polygon class="tier" points="254.7,933 549.3,933 569.6,981 234.4,981"/>
    <polygon class="tier" points="229.3,993 574.7,993 597.5,1047 206.5,1047"/>

    <line class="marker-line" x1="304" y1="657" x2="327" y2="657"/>
    <rect class="marker" x="327" y="646" width="21" height="21"/>

    <line class="marker-line" x1="503" y1="711" x2="526" y2="711"/>
    <rect class="marker" x="483" y="700" width="20" height="21"/>

    <line class="marker-line" x1="252" y1="778" x2="276" y2="778"/>
    <rect class="marker" x="276" y="768" width="21" height="20"/>

    <line class="marker-line" x1="555" y1="834" x2="580" y2="834"/>
    <rect class="marker" x="534" y="824" width="21" height="20"/>

    <line class="marker-line" x1="197" y1="900" x2="221" y2="900"/>
    <rect class="marker" x="221" y="890" width="22" height="20"/>

    <line class="marker-line" x1="608" y1="957" x2="633" y2="957"/>
    <rect class="marker" x="587" y="947" width="21" height="20"/>

    <line class="marker-line" x1="146" y1="1022" x2="170" y2="1022"/>
    <rect class="marker" x="170" y="1012" width="21" height="20"/>
  </svg>

  <span class="tier-label label-left" style="right:507px; top:644px;">Calories</span>
  <span class="tier-label" style="left:540px; top:698px;">Protien</span>
  <span class="tier-label label-left" style="right:563px; top:765px;">Food Quality</span>
  <span class="tier-label" style="left:588px; top:821px;">Meal</span>
  <span class="tier-label label-left" style="right:612px; top:887px;">Timing</span>
  <span class="tier-label" style="left:640px; top:944px;">Suppliments</span>
  <span class="tier-label label-left" style="right:662px; top:1009px;">Noise</span>

  <p class="author">Authors Name</p>
</main>
</body>
</html>
```